Business Card design for an International Import Export House

We need a Business Card design for our import export business. We trade in Minerals, Metals, Rice, Sugar, Steel etc.. The design should be minimalistic. It may or may not contain the physical address. In case you want to include the physical address - 418 Marwick Plaza, Oakvale Sector 7, Brightholm, Eastvale, India, 560417.

Target Market(s)

Steel Mills or Steel Plants, Factories, Mining businesses, Industrial houses, Government Agencies

Industry/Entity Type

Importer

Contact Information for Business Card

Business Name - Verrano Trade

Font styles to use
Other font styles liked:
• montserrat

Requirements
Must have
• Darin Pohlak - President
• www.verranotrade.example
• darin@verranotrade.example
• +91-988-412-3675
Nice to have
• worldwide suppliers of ores

```html
<!DOCTYPE html>
<html lang="en">
<head>
<meta charset="UTF-8">
<title>Verrano Trade – Business Card</title>
<link rel="stylesheet" href="https://fonts.googleapis.com/css2?family=Roboto:wght@300;400;700&display=swap">
<style>
  :root {
    --backdrop: #9b9b9b;
    --card: #f7f7f6;
    --ink: #1f1f1f;
    --ink-soft: #2b2b2b;
    --teal: #4d9eb2;
    --white: #ffffff;
  }
  * { box-sizing: border-box; margin: 0; padding: 0; }
  html, body {
    width: 1200px;
    height: 1200px;
    overflow: hidden;
  }
  body {
    background: var(--backdrop);
    display: flex;
    align-items: center;
    justify-content: center;
    font-family: "Roboto", Arial, sans-serif;
    color: var(--ink);
  }
  .business-card {
    position: relative;
    width: 1000px;
    height: 571px;
    background: var(--card);
    box-shadow: 0 12px 30px rgba(0, 0, 0, 0.18);
  }

  /* Brand name block */
  .brand {
    position: absolute;
    left: 90px;
    bottom: 130px;
    display: flex;
    align-items: center;
    gap: 16px;
  }
  .brand-dot {
    width: 40px;
    height: 40px;
    border-radius: 50%;
    background: var(--teal);
  }
  .brand-name {
    font-size: 30px;
    font-weight: 700;
    letter-spacing: -0.5px;
    text-transform: uppercase;
    color: var(--teal);
  }

  /* Person block */
  .person {
    position: absolute;
    right: 100px;
    top: 95px;
    text-align: right;
  }
  .person-name {
    font-size: 36px;
    font-weight: 300;
    color: var(--ink-soft);
    line-height: 1;
  }
  .person-title {
    font-size: 15px;
    font-weight: 700;
    color: var(--teal);
    margin-top: 4px;
    margin-right: -22px;
  }

  /* Contact lines, address last, all ending at the icon column */
  .contact-list {
    position: absolute;
    right: 70px;
    bottom: 48px;
    list-style: none;
  }
  .contact-item {
    display: flex;
    justify-content: flex-end;
    align-items: center;
    gap: 12px;
    font-size: 21px;
    font-weight: 400;
    line-height: 32px;
    color: var(--ink);
    white-space: nowrap;
  }
  .contact-icon {
    width: 18px;
    height: 18px;
    background: var(--teal);
    border-radius: 2px;
    display: flex;
    align-items: center;
    justify-content: center;
    flex-shrink: 0;
  }
  .contact-icon svg { width: 12px; height: 12px; }
</style>
</head>
<body>
  <main class="business-card">
    <section class="person">
      <h1 class="person-name">Darin Pohlak</h1>
      <p class="person-title">President</p>
    </section>

    <div class="brand">
      <span class="brand-dot"></span>
      <span class="brand-name">Verrano Trade</span>
    </div>

    <ul class="contact-list">
      <li class="contact-item">+91-988-412-3675
        <span class="contact-icon">
          <svg viewBox="0 0 12 12"><path d="M3 1 L5 3.5 L4 4.7 Q5 7 7.3 8 L8.5 7 L11 9 L9.8 10.8 Q5 11 1.2 3 Z" fill="var(--white)"/></svg>
        </span>
      </li>
      <li class="contact-item">www.verranotrade.example
        <span class="contact-icon">
          <svg viewBox="0 0 12 12" fill="none" stroke="var(--white)" stroke-width="1.2"><circle cx="6" cy="6" r="4.6"/><ellipse cx="6" cy="6" rx="2" ry="4.6"/><line x1="1.4" y1="6" x2="10.6" y2="6"/></svg>
        </span>
      </li>
      <li class="contact-item">darin@verranotrade.example
        <span class="contact-icon">
          <svg viewBox="0 0 12 12" fill="none" stroke="var(--white)" stroke-width="1.2"><rect x="1" y="2.5" width="10" height="7"/><polyline points="1,2.5 6,6.5 11,2.5"/></svg>
        </span>
      </li>
      <li class="contact-item">418 Marwick Plaza, Oakvale Sector 7, Brightholm, Eastvale, India, 560417
        <span class="contact-icon">
          <svg viewBox="0 0 12 12"><path d="M6 11 L2.8 6 A3.6 3.6 0 1 1 9.2 6 Z" fill="var(--white)"/><circle cx="6" cy="4.6" r="1.3" fill="var(--teal)"/></svg>
        </span>
      </li>
    </ul>
  </main>
</body>
</html>
```